QPLx 500mg CBD Tincture

We are rebranding and need new label ideas. I’m including our old label as reference to the bottle and the die lines.
Our company is called Alder Fern Company and we are a CBD company.

We would like a design for 1oz tincture bottle with a dropper. They are matte white with white tops. We have 2 flavors, peppermint and orange cream

I’ve uploaded the logo, colors and theme of the rebranding. We only want to use the Logos, no writing out of the company name. We are trying to shift to QPLx so that we can market more through the whole country.

We like clean and neat design. Elegant meets modern. Not cluttered. Our logo is new too so you can use that as an idea.

Requirements
Must have
• A neat and clean design. Something that is easily duplicated over other products over time.
Should not have
• My pro just must not have the company name written out. Only logo. No cannabis leaves.

```html
<!DOCTYPE html>
<html lang="en">
<head>
<meta charset="utf-8">
<title>QPLx 500mg CBD Tincture – Label</title>
<link rel="stylesheet" href="https://fonts.googleapis.com/css2?family=Montserrat:wght@300;400;700&family=Roboto+Condensed:wght@300;400&family=Caveat:wght@400&display=swap">
<style>
  :root {
    --page: #ffffff;
    --ink: #1e0d0d;
    --peach: #f8c6a9;
    --peach-strong: #f0a07a;
    --peach-text: #e48c62;
    --mint: #b3d9d6;
    --mint-strong: #86c8c4;
    --mint-text: #6fbab5;
    --grey-text: #555555;
    --white: #ffffff;
  }
  * { box-sizing: border-box; margin: 0; padding: 0; }
  html, body { width: 1114px; height: 1200px; overflow: hidden; background: var(--page); }
  body { position: relative; font-family: "Montserrat", sans-serif; color: var(--ink); }

  /* Front panels */
  .front-panel {
    position: absolute; top: 384px; width: 204px; height: 287px;
    background: var(--white); overflow: hidden;
    box-shadow: 0 1px 4px rgba(0,0,0,0.12);
  }
  .front-panel--orange { left: 224px; }
  .front-panel--mint { left: 640px; }
  .front-panel .wave { position: absolute; inset: 0; }
  .brand-seal {
    position: absolute; border-radius: 50%; background: var(--white);
    border: 1.5px solid var(--ink); display: flex; align-items: center; justify-content: center;
    font-family: "Montserrat", sans-serif; font-weight: 400; color: var(--ink);
  }
  .front-panel .brand-seal { left: 62px; top: 22px; width: 80px; height: 80px; font-size: 18px; }
  .product-name { position: absolute; left: 0; right: 0; text-align: center; font-weight: 700; color: var(--ink); letter-spacing: -0.5px; }
  .flavor { position: absolute; left: 0; right: 0; text-align: center; font-family: "Caveat", cursive; white-space: nowrap; }
  .spectrum { position: absolute; left: 0; right: 0; text-align: center; font-weight: 300; line-height: 1.25; }
  .net-weight {
    position: absolute; color: var(--white); font-weight: 300; text-align: center;
    display: flex; align-items: center; justify-content: center; white-space: nowrap;
  }
  .front-panel .product-name { top: 108px; font-size: 35px; }
  .front-panel .flavor { top: 160px; font-size: 33px; }
  .front-panel .spectrum { top: 210px; font-size: 13.5px; }
  .front-panel .net-weight { left: 38px; top: 265px; width: 128px; height: 22px; font-size: 11px; }
  .front-panel--orange .flavor, .front-panel--orange .spectrum { color: var(--peach-text); }
  .front-panel--orange .net-weight { background: var(--peach-strong); }
  .front-panel--mint .flavor { color: var(--mint-text); }
  .front-panel--mint .spectrum { color: var(--grey-text); }
  .front-panel--mint .net-weight { background: var(--mint-strong); }

  /* Full wrap label */
  .wrap-label {
    position: absolute; left: 130px; top: 795px; width: 828px; height: 361px;
    background: var(--white); overflow: hidden;
    box-shadow: 0 2px 6px rgba(0,0,0,0.18);
  }
  .wrap-label .wave { position: absolute; inset: 0; }
  .usage {
    position: absolute; left: 24px; top: 16px; width: 222px;
    font-family: "Roboto Condensed", sans-serif; font-size: 14.5px; line-height: 20px; text-align: justify;
  }
  .warning {
    position: absolute; left: 22px; top: 86px; width: 219px; height: 74px; padding: 8px 9px;
    background: var(--peach-strong); color: var(--white);
    font-family: "Roboto Condensed", sans-serif; font-size: 14.5px; line-height: 19.5px; text-align: justify;
  }
  .divider { position: absolute; left: 20px; top: 171px; width: 221px; border-top: 1px solid var(--peach-strong); }
  .qr-slot {
    position: absolute; left: 26px; top: 190px; width: 104px; height: 158px; background: var(--white);
    display: flex; align-items: center; justify-content: center; text-align: center;
    font-size: 22px; font-weight: 400; line-height: 27px;
  }
  .company-info {
    position: absolute; left: 146px; top: 187px;
    font-family: "Roboto Condensed", sans-serif; font-size: 16px; line-height: 20px;
  }
  .origin-badge { position: absolute; left: 146px; top: 251px; width: 46px; height: 46px; border-radius: 50%; background: #2c3e73; border: 2px solid #c9ced9; }
  .recycle-mark { position: absolute; left: 148px; top: 306px; width: 42px; height: 42px; }
  .wrap-label .brand-seal { left: 364px; top: 27px; width: 103px; height: 103px; font-size: 22px; }
  .wrap-label .product-name { top: 148px; font-size: 44px; }
  .wrap-label .flavor { top: 208px; font-size: 48px; color: var(--peach-text); }
  .wrap-label .spectrum { top: 270px; font-size: 18px; line-height: 21px; color: var(--peach-text); }
  .wrap-label .net-weight { left: 334px; top: 331px; width: 160px; height: 30px; font-size: 14.5px; background: var(--peach-strong); }
  .facts-table {
    position: absolute; left: 604px; top: 30px; width: 205px; background: var(--white);
    border: 1px solid var(--ink); font-family: "Roboto Condensed", sans-serif; color: var(--peach-text);
    font-weight: 300; font-size: 14px; line-height: 20px;
  }
  .facts-table .row { padding: 7px 8px; }
  .facts-table .row strong { font-weight: 400; }
  .facts-table .row--facts { min-height: 78px; border-bottom: 3px solid var(--ink); }
  .facts-table .row--serving { min-height: 57px; border-bottom: 1px solid var(--ink); }
  .facts-table .row--daily { min-height: 38px; padding-left: 11px; }
  .barcode-slot {
    position: absolute; left: 600px; top: 274px; width: 209px; height: 63px; background: var(--white);
    display: flex; align-items: center; justify-content: center; font-size: 22px; font-weight: 400;
  }
</style>
</head>
<body>

  <section class="front-panel front-panel--orange" aria-label="Orange Cream front panel">
    <svg class="wave" viewBox="0 0 204 287" preserveAspectRatio="none" aria-hidden="true">
      <path d="M0,80 C20,80 35,74 50,68 C90,52 130,58 160,55 C180,52 192,44 204,42 L204,287 L0,287 Z" fill="var(--peach)"/>
    </svg>
    <div class="brand-seal">QPLx</div>
    <h1 class="product-name">CBD OIL</h1>
    <p class="flavor">Orange Cream</p>
    <p class="spectrum">BROAD SPECTRUM<br>500 MG</p>
    <p class="net-weight">NT WT 1 FL OZ / 30 ml</p>
  </section>

  <section class="front-panel front-panel--mint" aria-label="Peppermint front panel">
    <svg class="wave" viewBox="0 0 204 287" preserveAspectRatio="none" aria-hidden="true">
      <path d="M0,80 C20,80 35,74 50,68 C90,52 130,58 160,55 C180,52 192,44 204,42 L204,287 L0,287 Z" fill="var(--mint)"/>
    </svg>
    <div class="brand-seal">QPLx</div>
    <h1 class="product-name">CBD OIL</h1>
    <p class="flavor">Peppermint</p>
    <p class="spectrum">BROAD SPECTRUM<br>500 MG</p>
    <p class="net-weight">NT WT 1 FL OZ / 30 ml</p>
  </section>

  <section class="wrap-label" aria-label="Orange Cream full wrap label">
    <svg class="wave" viewBox="0 0 828 361" preserveAspectRatio="none" aria-hidden="true">
      <path d="M0,92 C40,78 80,80 130,86 C200,94 250,98 290,92 C330,86 345,100 365,92 L470,80 C520,70 560,54 600,52 C680,48 760,60 790,80 C805,90 815,90 828,84 L828,361 L0,361 Z" fill="var(--peach)"/>
    </svg>

    <p class="usage">SUGGESTED USE: Lorem ipsum dolor sit amet, consectetuer adipi&shy;scing elit, sed diam nonummy.</p>
    <p class="warning">WARNING: Lorem ipsum dolor sit amet, consectetuer adipi&shy;scing elit, sed diam nonummy.</p>
    <div class="divider"></div>
    <div class="qr-slot">QR<br>CODE</div>
    <p class="company-info">Company<br>Address<br>Contact</p>
    <div class="origin-badge" role="img" aria-label="Origin badge"></div>
    <svg class="recycle-mark" viewBox="0 0 42 42" role="img" aria-label="Recyclable mark">
      <path d="M21,4 L38,36 L4,36 Z" fill="none" stroke="var(--peach-strong)" stroke-width="2"/>
    </svg>

    <div class="brand-seal">QPLx</div>
    <h1 class="product-name">CBD OIL</h1>
    <p class="flavor">Orange Cream</p>
    <p class="spectrum">BROAD SPECTRUM<br>500 MG</p>
    <p class="net-weight">NT WT 1 FL OZ / 30 ml</p>

    <div class="facts-table">
      <div class="row row--facts"><strong>Supplement facts</strong> Lorem ipsum dolor sit amet, consectetuer adipi&shy;scing elit, sed diam.</div>
      <div class="row row--serving"><strong>Serving size</strong> Lorem ipsum<br>dolor sit amet, consectetuer</div>
      <div class="row row--daily">Daily value not established</div>
    </div>
    <div class="barcode-slot">BAR CODE</div>
  </section>

</body>
</html>
```